home theater/ flat panel TV installation/ computer networking

single page flyer front and back, I am paying for adress labels so it should be 8 1/2" x 11" tri-fold with a place for the labels to go and be easy to mail.

Brightline Media

Charlotte NC 28391

http://www.brightlinemedianc.example/

call today for your no cost consultation  704-582-3946

Call today for your no cost consultation!    704-582-3946  Brightline Media

If your new home came with a finished basement, or you are

finishing it yourself, consider making part of it into a great home

theater. Why not add a fantastic High Definition projector and 100”

screen to your lovely new home? Experience satellite and cable TV,

video games, and of course, movies like you have never seen or

heard before. The cost of the system is probably a lot less than you

think. Finally, we install everything and provide a single programmed

remote to operate the entire system, easily! Already have a High

Definition TV? Let us integrate it with speakers, programmable

remotes, even a popcorn machine! Free consultations at your

request.

professional home theater designer and network cable installations in Texas

regular size.  I am picturing 8 1/2" x 11"  tri-fold.   I have never had a flyer before and am willing to accept different sizes.   

 

Target Market(s)

These will be sent to new home owners already looking for these services. I am a small company trying to say "we are the best".

These are the services we sell... (feel free to High-light or bullet)

-Home Theater
-High Definition TV
-Surround Sound
-All-in-One remotes
-Computer Networks
-Liscenced Electrician
-Lighting control

Industry/Entity Type

Computer

Requirements
Must have
• most of these photos. I am willing to pay for something better if available.  maybe a family or something.

• customer testimonial (should be italisized)

• "Brightline Media showed up on time, cleaned up after themselves, they we great!"

• "...we left the key under the mat, when we got home the TV was on the wall..."
Nice to have
• sonic wave from business card.eps file
• a few more photos

```html
<!DOCTYPE html>
<html lang="en">
<head>
<meta charset="utf-8">
<title>Brightline Media – Tri-fold Mailer</title>
<link rel="stylesheet" href="https://fonts.googleapis.com/css2?family=Montserrat:wght@400;500;600&family=Libre+Baskerville:ital,wght@0,700;1,400&display=swap">
<style>
  :root{
    --page-bg:#ffffff;
    --paper:#e4eef5;
    --paper-light:#f2f7fb;
    --brand-blue:#3d85bd;
    --band-blue:#5a8fb0;
    --ink:#3b4650;
    --ink-soft:#55616b;
    --white:#ffffff;
    --photo-dark:#2a2a2a;
    --frame:#8c959c;
  }
  *{box-sizing:border-box;margin:0;padding:0}
  html,body{width:1200px;height:1184px;overflow:hidden;background:var(--page-bg)}
  body{position:relative;font-family:"Montserrat",sans-serif;color:var(--ink)}

  .sheet{position:absolute;left:250px;width:700px;height:546px;overflow:hidden;
    background:linear-gradient(135deg,var(--paper-light) 0%,var(--paper) 60%,#d3e3ee 100%);
    box-shadow:0 1px 4px rgba(0,0,0,.25)}
  .sheet--outside{top:30px}
  .sheet--inside{top:608px}
  .abs{position:absolute}

  .photo{position:absolute}
  .photo--tv-wall{left:0;top:0;width:233px;height:546px;
    background:linear-gradient(160deg,#4a4a4a 0%,var(--photo-dark) 45%,#111 100%)}

  .stamp-box{left:410px;top:19px;width:30px;height:48px;background:var(--white)}
  .label-box{left:257px;top:270px;width:183px;height:75px;background:var(--white)}

  .brand{font-family:"Montserrat",sans-serif;font-weight:500;color:var(--brand-blue);white-space:nowrap;letter-spacing:.3px}
  .brand--cover{left:490px;top:170px;font-size:21px}
  .brand--return{left:292px;top:412px;font-size:14px}

  .return-info{left:233px;width:233px;text-align:center;color:var(--ink);top:448px}
  .return-info .city{font-size:8px;margin-left:-10px}
  .return-info .web{font-size:7px;margin-top:2px;margin-left:-10px}
  .return-info .cta{font-size:10px;margin-top:8px}
  .return-info .phone{font-size:17px;font-weight:500;margin-top:6px;letter-spacing:.5px}

  /* inside */
  .headline{left:22px;top:28px;font-size:11.5px;font-weight:600;color:var(--brand-blue);letter-spacing:.6px}
  .copy{font-size:10.5px;line-height:1.55;text-align:center;color:var(--ink)}
  .copy--intro{left:18px;top:78px;width:200px}
  .copy--detail{left:16px;top:240px;width:205px}
  .band{background:var(--band-blue);color:var(--white);font-size:9.5px;font-weight:500;text-transform:uppercase;text-align:center;line-height:1.5;letter-spacing:.3px;display:flex;align-items:center;justify-content:center}
  .band--projector{left:0;top:157px;width:233px;height:62px;padding:0 10px;font-size:9px;white-space:nowrap}
  .photo--remotes{left:45px;top:392px;width:168px;height:120px;
    background:radial-gradient(ellipse at center,#c9d6df 0%,#6e8aa0 55%,rgba(40,40,40,.0) 75%)}

  .services{left:259px;top:59px;width:200px;height:190px;background:var(--band-blue);color:var(--white);padding:14px 16px}
  .services h2{font-size:12px;font-weight:600;letter-spacing:.6px;margin-bottom:8px}
  .services ul{list-style:none;font-size:10.5px;line-height:1.9}
  .services li::before{content:"• "}

  .photo--theater{left:259px;top:265px;width:200px;height:144px;background:linear-gradient(180deg,#6b4a2e 0%,#3a2618 60%,#1e1510 100%)}
  .testimonial{left:259px;top:418px;width:198px}
  .testimonial h3{font-family:"Libre Baskerville",serif;font-size:10px;font-weight:700;color:var(--ink);margin-bottom:8px}
  .testimonial p{font-family:"Libre Baskerville",serif;font-style:italic;font-size:9px;line-height:1.5;color:var(--ink-soft);margin-bottom:8px}

  .photo--living{left:530px;top:0;width:170px;height:117px;background:linear-gradient(160deg,#c9a779 0%,#8d6a45 55%,#5c4430 100%)}
  .photo--wall-tv{left:465px;top:122px;width:63px;height:112px;background:linear-gradient(180deg,#5a4536 0%,#2e241d 100%)}
  .photo--lounge{left:532px;top:122px;width:168px;height:112px;background:linear-gradient(170deg,#a7755a 0%,#7a4e3a 55%,#4b3026 100%)}
  .band--hdtv{left:465px;top:252px;width:222px;height:40px}
  .copy--hdtv{left:470px;top:312px;width:212px}

  .consult{left:465px;top:378px;width:218px;height:144px;border:1.5px solid var(--frame);padding:12px 12px}
  .consult h2{font-size:11px;font-weight:600;line-height:1.45;color:var(--ink);text-transform:uppercase;letter-spacing:.3px}
  .consult .web{font-size:10px;margin-top:10px}
  .consult .cta{font-size:10px;margin-top:12px;line-height:1.5}
  .consult .cta strong{font-size:13px;font-weight:500}
</style>
</head>
<body>

<section class="sheet sheet--outside" aria-label="Mailer outside">
  <div class="photo photo--tv-wall" role="img" aria-label="Black and white photo of a wall of flat panel TVs showing a playground scene"></div>
  <div class="abs stamp-box" aria-label="Postage area"></div>
  <div class="abs label-box" aria-label="Address label area"></div>
  <div class="abs brand brand--cover">Brightline Media</div>
  <div class="abs brand brand--return">Brightline Media</div>
  <div class="abs return-info">
    <p class="city">Charlotte NC 28391</p>
    <p class="web">www.brightlinemedianc.example</p>
    <p class="cta">Call today for your no cost consultation</p>
    <p class="phone">704-582-3946</p>
  </div>
</section>

<section class="sheet sheet--inside" aria-label="Mailer inside">
  <h1 class="abs headline">EXPERIENCE, PROFESSIONAL AND RELIABLE.</h1>
  <p class="abs copy copy--intro">If your new home came with a finished basement, or you are finishing it yourself, consider making part of it into a great home theater.</p>
  <div class="abs band band--projector">Why not add a fantastic high<br>definition projector and 100"<br>screen to your lovely new home?</div>
  <p class="abs copy copy--detail">Experience satellite and cable TV, video games, and of course, movies like you have never seen or heard before. The cost of the system is probably a lot less than you think. Finally, we install everything and provide a single programmed remote to operate the entire system, easily!</p>
  <div class="photo photo--remotes" role="img" aria-label="Photo of three universal remote controls"></div>

  <div class="abs services">
    <h2>SERVICES WE SELL</h2>
    <ul>
      <li>Home Theater</li>
      <li>High Definition TV</li>
      <li>Surround Sound</li>
      <li>All-in-One remotes</li>
      <li>Computer Networks</li>
      <li>Licensed Electrician</li>
      <li>Lighting control</li>
    </ul>
  </div>
  <div class="photo photo--theater" role="img" aria-label="Photo of a home theater room with leather recliners"></div>
  <div class="abs testimonial">
    <h3>Customer Testimonial</h3>
    <p>"Brightline Media showed up on time, cleaned up after themselves, they we great!"</p>
    <p>"...we left the key under the mat, when we got home the TV was on the wall..."</p>
  </div>

  <div class="photo photo--living" role="img" aria-label="Photo of a living room with a TV above a brick fireplace"></div>
  <div class="photo photo--wall-tv" role="img" aria-label="Photo of a wall mounted TV in a den"></div>
  <div class="photo photo--lounge" role="img" aria-label="Photo of a media lounge with sofas"></div>
  <div class="abs band band--hdtv">Already have a high definition TV?</div>
  <p class="abs copy copy--hdtv">Let us integrate it with speakers, programmable remotes, even a popcorn machine!</p>
  <div class="abs consult">
    <h2>Free consultations<br>at your request.</h2>
    <p class="web">www.brightlinemedianc.example</p>
    <p class="cta">Call today for your no cost consultation at <strong>704-582-3946</strong></p>
  </div>
</section>

</body>
</html>
```